CoveysArmsPersonal

I am a cutting edge, top of the line gun store. We are expanding faster than we can keep up. We offer: Gunsmithing, Transfers, Concealed Carry, Machine Guns, Suppressors. My colors are reflected in my logo. Red, black and white. I like a clean design that gets the point across. I was trying to find a plastic business card, but will settle with a high quality paper product.

Contact Information for Business Card

Dwayne Covey - Owner
620-514-8826 (Cell)
Covey's Range Outfitters
1847 E. Hwy 9
Pine Hollow, NE 67462
sales@coveysrangeoutfitters.com
coveysrangeoutfitters.com

```html
<!DOCTYPE html>
<html lang="en">
<head>
<meta charset="utf-8">
<title>Covey's Range Outfitters – Business Card</title>
<link rel="stylesheet" href="https://fonts.googleapis.com/css2?family=Open+Sans:wght@400;600&family=Share+Tech+Mono&display=swap">
<style>
  :root {
    --backdrop: #e4e5e6;
    --card-black: #151515;
    --card-black-soft: #222222;
    --panel-grey: #b9b9b9;
    --panel-grey-light: #cdcdcd;
    --panel-ink: #1c1c1c;
    --band-slate: #2e3236;
    --band-slate-light: #4a4f55;
    --band-ink: #c9c9c9;
    --brand-red: #8e1d22;
    --brand-silver: #9a9a9a;
  }
  * { box-sizing: border-box; margin: 0; padding: 0; }
  html, body {
    width: 1200px;
    height: 900px;
    overflow: hidden;
    background: var(--backdrop);
  }
  .stage {
    width: 1200px;
    height: 900px;
    display: flex;
    align-items: center;
    justify-content: center;
  }
  .business-card {
    position: relative;
    width: 440px;
    height: 740px;
    border-radius: 6px;
    background: radial-gradient(ellipse at 40% 35%, var(--card-black-soft), var(--card-black) 70%);
    box-shadow: 0 10px 30px rgba(0,0,0,0.25);
    overflow: hidden;
  }
  .contact-panel {
    position: absolute;
    top: 22px;
    left: 148px;
    width: 272px;
    height: 300px;
    border-radius: 4px 4px 18px 4px;
    background: linear-gradient(160deg, var(--panel-grey-light), var(--panel-grey));
    padding: 26px 16px 0 18px;
    font-family: "Open Sans", sans-serif;
    color: var(--panel-ink);
  }
  .contact-panel .address {
    font-size: 14px;
    line-height: 20px;
    margin-bottom: 14px;
    white-space: nowrap;
  }
  .contact-panel .phone {
    font-size: 17px;
    font-weight: 600;
    margin-bottom: 14px;
    white-space: nowrap;
  }
  .contact-panel .web {
    font-size: 14px;
    line-height: 21px;
    white-space: nowrap;
  }
  .name-band {
    position: absolute;
    top: 262px;
    left: 36px;
    width: 404px;
    height: 92px;
    background: linear-gradient(90deg, var(--band-slate), var(--band-slate-light) 55%, var(--band-slate));
    box-shadow: 0 4px 10px rgba(0,0,0,0.5);
    padding: 10px 0 0 40px;
    font-family: "Share Tech Mono", monospace;
    color: var(--band-ink);
  }
  .name-band .person-name {
    font-size: 36px;
    letter-spacing: 3px;
    line-height: 40px;
    white-space: nowrap;
  }
  .name-band .person-role {
    font-size: 30px;
    letter-spacing: 3px;
    line-height: 34px;
  }
  .brand-lockup {
    position: absolute;
    top: 450px;
    left: 0;
    width: 440px;
    display: flex;
    flex-direction: column;
    align-items: center;
    gap: 26px;
  }
  .brand-mark {
    width: 70px;
    height: 70px;
  }
  .brand-name {
    font-family: "Share Tech Mono", monospace;
    font-size: 25px;
    letter-spacing: 1px;
    color: var(--brand-silver);
    text-align: center;
    white-space: nowrap;
  }
</style>
</head>
<body>
  <main class="stage">
    <article class="business-card">
      <section class="contact-panel">
        <p class="address">Covey's Range Outfitters 1847<br>E. Hwy 9 Pine Hollow NE 67462</p>
        <p class="phone">Contact : 620-514-8826</p>
        <p class="web">coveysrangeoutfitters.com<br>sales@coveysrangeoutfitters.com</p>
      </section>
      <header class="name-band">
        <p class="person-name">Dwayne Covey</p>
        <p class="person-role">Owner</p>
      </header>
      <div class="brand-lockup">
        <svg class="brand-mark" viewBox="0 0 70 70" aria-hidden="true">
          <circle cx="35" cy="35" r="32" fill="var(--brand-red)"/>
        </svg>
        <p class="brand-name">Covey's Range Outfitters</p>
      </div>
    </article>
  </main>
</body>
</html>
```